BRELM - Letterhead

Willowmere Institute of Letters and Crafts (BRELM) is a non-profit organization that operates two tuition-free public schools - BRELM Elementary for grades K to 5th and BRELM College Prep for grades 6-12.

We are looking for a letterhead primarily to be used on Google Docs and Microsoft Word. Attached are two versions of our logo. One with our name spelled out and one with the acronym.

For Letterhead, we would like 3 addresses listed:

BRELM HQ
41872 Hollow Brook Lane, Suite 308
Laguna Niguel, CA 92677

BRELM Elementary (K-5)
18460 Marsh Ridge Boulevard
Laguna Niguel, CA 92677

BRELM College Prep (6-12)
27314 Del Sol Terrace
San Juan Capistrano, CA 92675

Our Phone Number is (555) 418-7062
Our Fax Number is the same (555) 418-7062

Our website is www.brelmschools.org

Target Market(s)

Education

Industry/Entity Type

Education

Font styles to use
Sans Serif

Colors
0054AA
0677BA
7BADD7
CADEEF
E8F1F8

Requirements
Must have
• Logo, Address, Phone Number, Website.
Nice to have
• Modern and clean design.
Should not have
• Prefer that there is no bleed -- the letterhead will mostly be used in PDF format however sometimes it will be printed and our printers can not do a full bleed

```html
<!DOCTYPE html>
<html lang="en">
<head>
<meta charset="utf-8">
<title>BRELM Letterhead</title>
<link rel="stylesheet" href="https://fonts.googleapis.com/css2?family=Nunito+Sans:wght@400;600;700&family=Arimo:wght@400&display=swap">
<style>
  :root {
    --backdrop: #ece8e2;
    --paper: #f7f7f8;
    --ink: #1b1b1b;
    --body-ink: #4a4a4a;
    --navy: #0a3d9a;
    --blue: #0a7cc4;
    --green: #1a9a3c;
    --yellow: #e0b800;
    --red: #ec5a3a;
    --band: #0a3ea0;
    --rule: #333;
  }
  * { margin: 0; padding: 0; box-sizing: border-box; }
  html, body { width: 1200px; height: 1141px; overflow: hidden; background: var(--backdrop); }
  .letterhead {
    position: absolute; left: 208px; top: 20px; width: 784px; height: 1101px;
    background: var(--paper); box-shadow: 0 2px 10px rgba(0,0,0,.12);
    font-family: "Nunito Sans", sans-serif; color: var(--ink);
  }
  .brand {
    position: absolute; left: 54px; top: 96px;
    display: flex; align-items: center; gap: 6px;
    font-family: "Nunito Sans", sans-serif; font-weight: 600; font-size: 27px;
    color: var(--navy); letter-spacing: .5px;
  }
  .brand-mark { width: 12px; height: 12px; background: var(--navy); }
  .address { position: absolute; top: 98px; font-size: 11px; line-height: 13.3px; }
  .address strong { font-weight: 700; display: block; }
  .address.hq { left: 186px; }
  .address.elementary { left: 373px; }
  .address.prep { left: 559px; }
  .divider { position: absolute; top: 96px; width: 1px; height: 47px; background: var(--rule); }
  .divider.one { left: 358px; } .divider.two { left: 544px; }
  .color-bar { position: absolute; left: 186px; top: 151px; width: 541px; height: 3px; display: flex; gap: 2px; }
  .color-bar span { flex: 1; }
  .contact { position: absolute; left: 186px; top: 167px; display: flex; align-items: center; font-size: 13.2px; }
  .contact svg { width: 10px; height: 10px; margin-right: 8px; }
  .contact .item { display: flex; align-items: center; margin-right: 13px; }
  .letter { position: absolute; left: 57px; top: 0; width: 668px; font-family: "Arimo", sans-serif; color: var(--body-ink); }
  .salutation { position: absolute; top: 274px; font-size: 19px; color: #444; white-space: nowrap; }
  .body { position: absolute; top: 325px; width: 668px; font-size: 11.1px; line-height: 16.8px; text-align: justify; }
  .body p + p { margin-top: 16.6px; }
  .closing { position: absolute; top: 700px; font-size: 11.1px; }
  .signature { position: absolute; left: -4px; top: 738px; width: 226px; height: 68px; background: linear-gradient(90deg, rgba(40,40,40,.18), rgba(40,40,40,.06)); }
  .footer-emblems { position: absolute; left: 248px; top: 1037px; width: 251px; height: 54px; background: linear-gradient(90deg, var(--yellow), var(--red), var(--green), var(--blue), var(--navy)); }
  .footer-band { position: absolute; left: 0; bottom: 0; width: 100%; height: 25px; background: var(--band); }
</style>
</head>
<body>
<main class="letterhead">
  <div class="brand"><span class="brand-mark"></span>BRELM</div>

  <div class="address hq"><strong>BRELM HQ</strong>41872 Hollow Brook Lane, Suite<br>308, Laguna Niguel, CA 92677</div>
  <div class="divider one"></div>
  <div class="address elementary"><strong>BRELM Elementary (K-5)</strong>18460 Marsh Ridge Boulevard<br>Laguna Niguel, CA 92677</div>
  <div class="divider two"></div>
  <div class="address prep"><strong>BRELM College Prep (6-12)</strong>27314 Del Sol Terrace<br>San Juan Capistrano, CA 92675</div>

  <div class="color-bar">
    <span style="background:var(--navy)"></span><span style="background:var(--blue)"></span><span style="background:var(--green)"></span><span style="background:var(--yellow)"></span><span style="background:var(--red)"></span>
  </div>

  <div class="contact">
    <div class="item"><svg viewBox="0 0 10 10"><path d="M2 0.5 L3.6 2.6 L2.7 3.6 Q3.6 5.8 6.4 7.3 L7.4 6.4 L9.5 8 L8.3 9.5 Q1 7.5 0.5 1.7 Z" fill="var(--navy)"/></svg>(555) 418-7062</div>
    <div class="item"><svg viewBox="0 0 10 10"><rect x="0" y="2" width="10" height="7" fill="var(--navy)"/><path d="M0.5 2.5 L5 6 L9.5 2.5" stroke="#fff" stroke-width="1" fill="none"/></svg>(555) 418-7062</div>
    <div class="item"><svg viewBox="0 0 10 10" fill="none" stroke="var(--navy)" stroke-width=".8"><circle cx="5" cy="5" r="4.5"/><ellipse cx="5" cy="5" rx="2" ry="4.5"/><path d="M0.5 5 H9.5 M1.2 2.8 H8.8 M1.2 7.2 H8.8"/></svg>www.brelmschools.org</div>
  </div>

  <section class="letter">
    <div class="salutation">Dear Mr. Smith,</div>
    <div class="body">
      <p>Lorem ipsum dolor sit amet, consectetur adipiscing elit. Donec orci purus, luctus vitae dignissim eu, iaculis sed purus. Vivamus faucibus, ipsum nec aliquet viverra, leo mauris condimentum ligula, sit amet sagittis enim ligula quis arcu. Nam egestas tortor id nisi porttitor mattis. In tortor ante, ultricies in suscipit a, tempus non massa. Vivamus et auctor mi. Fusce vel massa nulla. Phasellus nec eros mauris, et scelerisque orci.</p>
      <p>Donec malesuada orci vitae nulla accumsan porta a id massa. Quisque accumsan iaculis magna sit amet fringilla. Maecenas consequat, magna eget tincidunt semper, odio nibh rutrum mi, id feugiat ante nisi eu risus. Vestibulum nunc orci, rhoncus a placerat in, ultricies in mi. Cras mattis varius eros, vel fringilla nisi suscipit eget. Quisque scelerisque sagittis nulla at porttitor.</p>
      <p>Sed id augue vitae urna euismod commodo aliquet a quam. Pellentesque arcu velit, cursus et malesuada ut, consequat et diam. Nullam erat sem, rhoncus id ullamcorper vitae, rhoncus et arcu. In ultricies ultricies nulla, ut rutrum nisi iaculis at. Donec eu magna a metus ornare faucibus. Fusce aliquet faucibus ultricies. Morbi semper, est id tincidunt gravida, sem arcu adipiscing lacus, ac bibendum nulla leo eu purus. Quisque nec diam sed risus consectetur a ccumsan quis quis nibh. Vestibulum id purus lorem.</p>
      <p>It is a long established fact that a reader will be distracted by the readable content of a page when looking at its layout. The point of using Lorem Ipsum is that it has a more-or-less normal distribution of letters, as opposed to using 'Content here, content here', making it look like readable English. Many desktop publishing packages</p>
      <p>ada ut, consequat et diam. Nullam erat sem, rhoncus id ullamcorper vitae, rhoncus et arcu. In ultricies ultricies nulla, ut rutrum nisi iaculis at. Donec eu magna a metus ornare faucibus. Fusce aliquet faucibus ultricies. Morbi semper,</p>
    </div>
    <div class="closing">Sincerely,</div>
    <div class="signature" role="img" aria-label="Handwritten signature of the sender"></div>
  </section>

  <div class="footer-emblems" role="img" aria-label="Row of five coloured school emblems"></div>
  <div class="footer-band"></div>
</main>
</body>
</html>
```